Tutoring center for k-12 and adults. ( name: Birch Tutoring )

We will start a tutoring center mainly teaching international students English, math, test prep ( SAT,ACT) for K-12 and English conversation class and English grammar for adults. Our mission and description is well described in the attached file below.
Our center is located in Ann Arbor Michigan, and will provide highly qualified instructors.
Our motto is " school like a home and teacher like parents" and "Birch Tutoring is the passage to success" and "Learn to think" I want you to have these main themes as designing the website, and we already have a designed logo attached below in the file. As the name shows, greenish, fresh feeling, but academically informative design is strongly recommended.
I want to emphasize warm and caring atmosphere of our center with the images fitting to this concept.

Target Market(s)

international students (k-12) and adults for ESL classes / high school students both American and international students for test preps: ACT,SAT

Industry/Entity Type

Education

Coding

Coded - Design and coding required

Number of Pages Required

3 page

Font styles to use
Serif
Sans Serif
Script

Requirements
Must have
• I think there are many options in my website to create different things, but at this point, I just want to make four headings on the top- Home, About us, Classes, Support.
• Home page includes mission statement, testimonial, brief introduction of Test prep classes (SAT,ACT), academic tutoring, and adults classes. Also logo and contact info should be located in the first page. As a second page (heading), classes need to be introduced. I wonder if I can insert Korean for Korean classes. In this section, I want to put class descriptions of each class. As a third heading, About us includes introduction of instructors with their educational background, and please make two more open spots for instructors because we will add more faculties later.
• As the last heading, Support is the section for Q &A and provide the address and map of the center. This part is optional if I go with 3 pages of website!
• It should be informative and simple, easy to find the necessary info.
• If I can update the info by semester or periodically by myself. If it's easy to aces to change and manage the info for me, it will be great.
Nice to have
• .
• If I can have an option to convert the language of the website from English to Korean or to Chinese, it will be very nice.
Should not have
• lesson fees

```html
<!DOCTYPE html>
<html lang="en">
<head>
<meta charset="utf-8">
<title>Birch Tutoring</title>
<link href="https://fonts.googleapis.com/css2?family=Montserrat:wght@200;300;400;500;600&display=swap" rel="stylesheet">
<style>
:root{
  --lime:#7cc21c;
  --ink:#1f2b3a;
  --muted:#8a919c;
  --paper:#f3f5f8;
  --white:#ffffff;
  --navy:#1c5a8e;
  --charcoal:#2f3031;
  --line:#e3e6ea;
}
*{box-sizing:border-box;margin:0;padding:0}
html,body{width:1200px;height:2214px;overflow:hidden}
body{position:relative;font-family:"Montserrat",sans-serif;color:var(--ink);background:var(--paper)}
.abs{position:absolute}

/* Hero */
.hero{left:0;top:0;width:1200px;height:521px;overflow:hidden}
.hero-art{position:absolute;inset:0;background:radial-gradient(ellipse 60% 85% at 50% 70%,#c9a76b 0%,#8a6a36 35%,#3a2a14 70%,#140e08 100%)}
.brand{position:absolute;left:241px;top:12px;width:90px;text-align:center;color:var(--white)}
.brand-mark{display:block;width:40px;height:40px;margin:0 auto 6px;border:2px solid var(--white);border-radius:50%}
.brand-name{font-size:11px;font-weight:500;letter-spacing:.02em;white-space:nowrap}
.nav{position:absolute;top:44px;left:686px;display:flex;gap:0;font-size:10px;font-weight:600;color:var(--white);text-transform:uppercase}
.nav a{color:inherit;text-decoration:none;position:absolute;white-space:nowrap}
.hero-title{position:absolute;left:0;width:1200px;top:258px;text-align:center;color:var(--white);font-size:31px;font-weight:300;letter-spacing:.95em;padding-left:.95em}

/* Section headings */
.section-title{position:absolute;left:0;width:1200px;text-align:center;font-size:26px;font-weight:200;color:var(--ink);letter-spacing:.02em;text-transform:uppercase}

/* Classes */
.classes{left:0;top:521px;width:1200px;height:322px;background:var(--paper)}
.class-item{position:absolute;top:117px;width:200px;margin-left:-100px;text-align:center}
.class-icon{display:block;margin:0 auto;width:60px;height:60px}
.class-name{margin-top:16px;font-size:10px;font-weight:500;letter-spacing:.06em;text-transform:uppercase}
.class-desc{margin-top:4px;font-size:8.5px;line-height:12px;color:var(--muted)}
.class-link{display:block;margin-top:10px;font-size:9px;font-weight:500;letter-spacing:.05em;color:var(--ink);text-decoration:none;text-transform:uppercase}

/* About */
.about{left:0;top:843px;width:1200px;height:289px;background:var(--navy)}
.about .section-title{color:var(--white);top:48px}
.about-text{position:absolute;left:320px;width:560px;top:106px;text-align:center;color:var(--white);font-size:13.4px;line-height:19.8px;font-weight:500}

/* Blog */
.blog{left:0;top:1132px;width:1200px;height:274px;background:var(--paper)}
.post{position:absolute;top:108px;width:220px;height:99px;background:var(--white);border:1px solid var(--line)}
.post-thumb{position:absolute;left:15px;top:17px;width:65px;height:63px}
.post-title{position:absolute;left:96px;top:18px;font-size:12.5px;color:var(--ink)}
.post-excerpt{position:absolute;left:96px;top:40px;width:115px;font-size:7.5px;line-height:12px;color:var(--muted)}

/* Testimonials */
.testimonials{left:0;top:1406px;width:1200px;height:352px;background:var(--paper);overflow:hidden}
.quote-card{position:absolute;top:0;width:596px;height:290px;background:var(--white)}
.quote-text{position:absolute;left:40px;right:40px;top:62px;text-align:center;font-size:29px;line-height:38px;font-weight:200;color:#7d8490}
.quote-author{position:absolute;left:0;right:0;top:228px;text-align:center;font-size:8.5px;letter-spacing:.05em;color:var(--ink);text-transform:uppercase}
.quote-mark{position:absolute;font-size:34px;font-weight:500;color:#c6ccd3;line-height:1}
.quote-open{left:26px;top:26px}
.quote-close{right:26px;top:234px}

/* Footer */
.footer{left:0;top:1758px;width:1200px;height:456px;background:var(--charcoal)}
.footer-title{position:absolute;top:40px;font-size:13.5px;font-weight:400;color:var(--white);text-transform:uppercase;letter-spacing:.02em}
.footer-text{position:absolute;left:241px;top:82px;width:330px;font-size:11.6px;line-height:20px;color:var(--white)}
.footer-contact{position:absolute;left:241px;top:157px;font-size:11.6px;line-height:20px;color:var(--white)}
.field{position:absolute;left:611px;width:347px;border:1px solid rgba(255,255,255,.12);background:rgba(255,255,255,.03);font-size:11px;color:rgba(255,255,255,.5);padding:10px 10px}
.send-btn{position:absolute;left:611px;top:320px;width:130px;height:34px;background:var(--lime);color:var(--white);font-size:11.5px;font-weight:500;text-transform:uppercase;text-align:center;line-height:34px;letter-spacing:.03em}
.footer-rule{position:absolute;left:0;top:387px;width:1200px;height:1px;background:rgba(255,255,255,.08)}
.copyright{position:absolute;left:241px;top:417px;font-size:8px;color:rgba(255,255,255,.35)}
.social{position:absolute;top:415px;width:14px;height:14px;border-radius:50%;background:rgba(255,255,255,.35)}
</style>
</head>
<body>

<header class="abs hero">
  <div class="hero-art" role="img" aria-label="Photograph of an open book with its pages fanned out in warm golden light"></div>
  <div class="brand">
    <span class="brand-mark"></span>
    <span class="brand-name">Birch Tutoring</span>
  </div>
  <nav class="nav">
    <a href="#" style="left:0">Home</a>
    <a href="#" style="left:54px">About us</a>
    <a href="#" style="left:127px">Classes</a>
    <a href="#" style="left:194px">Support</a>
    <svg style="position:absolute;left:260px;top:-3px" width="16" height="16" viewBox="0 0 16 16" fill="none" stroke="#fff" stroke-width="1.5"><circle cx="6.5" cy="6.5" r="5"/><path d="M10.3 10.3L15 15"/></svg>
  </nav>
  <h1 class="hero-title">Learn to think</h1>
</header>

<section class="abs classes">
  <h2 class="section-title" style="top:58px">Fall Classes</h2>

  <div class="class-item" style="left:362px">
    <svg class="class-icon" viewBox="0 0 60 60"><circle cx="30" cy="30" r="27" fill="var(--lime)"/><g stroke="#fff"><path d="M30 3V57M3 30H57" stroke-width="9"/><path d="M11 11L49 49M49 11L11 49" stroke-width="4"/></g></svg>
    <div class="class-name">English</div>
    <div class="class-desc">K-12 / Adults<br>Reading / Writing / Grammar</div>
    <a class="class-link" href="#">Learn more</a>
  </div>

  <div class="class-item" style="left:604px">
    <svg class="class-icon" viewBox="0 0 60 60" fill="none" stroke="var(--lime)" stroke-width="3.5" stroke-linejoin="round"><path d="M12 16L20 8L52 40L44 48Z"/><path d="M44 48L54 52L52 40"/><path d="M8 44L44 8L52 16L16 52Z"/><path d="M20 32l4 4M28 24l4 4M36 16l4 4"/></svg>
    <div class="class-name">Mathematics</div>
    <div class="class-desc">Lorem ipsum dolor sit amet, consecte-<br>tur adipisicing elit</div>
    <a class="class-link" href="#">Learn more</a>
  </div>

  <div class="class-item" style="left:838px">
    <svg class="class-icon" viewBox="0 0 60 60" fill="none" stroke="var(--lime)" stroke-width="3"><ellipse cx="30" cy="30" rx="27" ry="10"/><ellipse cx="30" cy="30" rx="27" ry="10" transform="rotate(60 30 30)"/><ellipse cx="30" cy="30" rx="27" ry="10" transform="rotate(120 30 30)"/><circle cx="30" cy="30" r="5" fill="var(--lime)"/></svg>
    <div class="class-name">Physics</div>
    <div class="class-desc">Lorem ipsum dolor sit amet, consecte-<br>tur adipisicing elit</div>
    <a class="class-link" href="#">Learn more</a>
  </div>
</section>

<section class="abs about" role="img" aria-label="Blue band with a faint pattern of school and science line icons">
  <h2 class="section-title">About Us</h2>
  <p class="about-text">Lorem ipsum dolor sit amet, consectetur adipisicing elit, sed do eiusmod tempor incididunt ut labore et dolore magna aliqua. Ut enim ad minim veniam, quis nostrud exercitation ullamco laboris nisi ut aliquip ex ea commodo consequat. Duis aute irure dolor in reprehenderit in voluptate velit esse cillum dolore eu fugiat nulla pariatur. Excepteur sint occaecat cupidatat non proident, sunt in culpa qui officia deserunt mollit anim id est laborum.</p>
</section>

<section class="abs blog">
  <h2 class="section-title" style="top:55px">Blog</h2>
  <article class="post" style="left:241px">
    <div class="post-thumb" role="img" aria-label="Photo of a student reading a book" style="background:linear-gradient(160deg,#8fb8c9,#3f3a33)"></div>
    <h3 class="post-title">Lorem ipsum</h3>
    <p class="post-excerpt">Lorem ipsum dolor sit amet consectetur adipisicing elit, sed do eiusmod tempor.</p>
  </article>
  <article class="post" style="left:489px">
    <div class="post-thumb" role="img" aria-label="Photo of an open book on a table" style="background:linear-gradient(180deg,#2a2522,#b9a58c 60%,#4a2f22)"></div>
    <h3 class="post-title">Lorem ipsum</h3>
    <p class="post-excerpt">Lorem ipsum dolor sit amet consectetur adipisicing elit, sed do eiusmod tempor.</p>
  </article>
  <article class="post" style="left:739px">
    <div class="post-thumb" role="img" aria-label="Black and white photo of library shelves" style="background:linear-gradient(90deg,#1c1c1c,#9a9a9a,#2b2b2b)"></div>
    <h3 class="post-title">Lorem ipsum</h3>
    <p class="post-excerpt">Lorem ipsum dolor sit amet consectetur adipisicing elit, sed do eiusmod tempor.</p>
  </article>
</section>

<section class="abs testimonials">
  <figure class="quote-card" style="left:-313px">
    <span class="quote-mark quote-open">&ldquo;</span>
    <blockquote class="quote-text">Lorem ipsum dolor sit amet, con-sectetur adipisicing elit, sed do eiusmod tempor incididunt ut labore et dolore magna aliqua.</blockquote>
    <figcaption class="quote-author">John Doe</figcaption>
    <span class="quote-mark quote-close">&rdquo;</span>
  </figure>
  <figure class="quote-card" style="left:301px">
    <span class="quote-mark quote-open">&ldquo;</span>
    <blockquote class="quote-text">Lorem ipsum dolor sit amet, con-sectetur adipisicing elit, sed do eiusmod tempor incididunt ut labore et dolore magna aliqua.</blockquote>
    <figcaption class="quote-author">John Doe</figcaption>
    <span class="quote-mark quote-close">&rdquo;</span>
  </figure>
  <figure class="quote-card" style="left:917px">
    <span class="quote-mark quote-open">&ldquo;</span>
    <blockquote class="quote-text">Lorem ipsum dolor sit amet, con-sectetur adipisicing elit, sed do eiusmod tempor incididunt ut labore et dolore magna aliqua.</blockquote>
    <figcaption class="quote-author">John Doe</figcaption>
    <span class="quote-mark quote-close">&rdquo;</span>
  </figure>
</section>

<footer class="abs footer" role="img" aria-label="Dark band with a faint pattern of colourful school and science line icons">
  <h2 class="footer-title" style="left:241px">Contact</h2>
  <p class="footer-text">Lorem ipsum dolor sit amet, consectetur adipisicing elit, sed do eiusmod tempor incididunt ut labore et dolore magna aliqua.</p>
  <p class="footer-contact">Email: hello@birchtutoring.com<br>Telephone: 1 23 555 0199</p>

  <h2 class="footer-title" style="left:608px">Contact us</h2>
  <div class="field" style="top:82px;height:34px">Email</div>
  <div class="field" style="top:131px;height:34px">Phone Number</div>
  <div class="field" style="top:179px;height:122px">Message</div>
  <div class="send-btn">Send message</div>

  <div class="footer-rule"></div>
  <p class="copyright">© 2015 Birch Tutoring. All Rights Reserved.</p>
  <span class="social" style="left:830px" aria-label="Social profile"></span>
  <span class="social" style="left:868px" aria-label="Social profile"></span>
  <span class="social" style="left:907px" aria-label="Social profile"></span>
  <span class="social" style="left:943px" aria-label="Social profile"></span>
</footer>

</body>
</html>
```